Makeup Artist

Hi I am makeup artist I attached the business card that I found on the net love the design.
I would love something like this simple but looking expensive.
I want double side business card. Front my full name. my phone number, email address and facebook and my next appointment is... on the other side.
Thank you :)

Hello I change my Facebook account - Makeup by Kolina, if you could please update your designs , thank you

Target Market(s)

high end clientele

Industry/Entity Type

Business

Colors
ec2027
ffc214
33b7a4
6b449b
e34197
9bcb3c
f37122
a64599

Requirements
Must have
• bright colours
Should not have
• brushes or whole lipsticks

```html
<!DOCTYPE html>
<html lang="en">
<head>
<meta charset="utf-8">
<title>Kolina Varenko – Makeup Artist Business Card</title>
<link href="https://fonts.googleapis.com/css2?family=Dancing+Script:wght@500&family=Quicksand:wght@400&family=Caveat:wght@400&display=swap" rel="stylesheet">
<style>
  :root {
    --page: #ffffff;
    --card-light: #f2f2f2;
    --card-mid: #b4b4b4;
    --card-dark: #6f6f6f;
    --lip-deep: #8e0b12;
    --lip-red: #cc1a22;
    --lip-bright: #e2333a;
    --name-red: #c20f1b;
    --note-red: #e8262d;
    --ink: #111111;
  }
  html, body {
    margin: 0;
    padding: 0;
    width: 1200px;
    height: 1000px;
    overflow: hidden;
    background: var(--page);
  }
  .sheet {
    position: relative;
    width: 1200px;
    height: 1000px;
  }
  .card-front {
    position: absolute;
    width: 575px;
    height: 288px;
    background: radial-gradient(ellipse 60% 62% at 52% 55%, var(--card-light) 0%, var(--card-mid) 62%, var(--card-dark) 100%);
    overflow: hidden;
  }
  .card-front--one { left: 20px; top: 18px; }
  .card-front--two { left: 554px; top: 330px; }
  .lipstick-photo {
    position: absolute;
    left: 38px;
    top: 16px;
    width: 170px;
    height: 242px;
    border-radius: 48% 52% 40% 46% / 30% 30% 55% 60%;
    background: linear-gradient(150deg, var(--lip-bright) 0%, var(--lip-red) 45%, var(--lip-deep) 100%);
  }
  .brand-name {
    position: absolute;
    right: 52px;
    top: 108px;
    margin: 0;
    font-family: "Dancing Script", cursive;
    font-weight: 500;
    font-size: 46px;
    letter-spacing: 2px;
    color: var(--name-red);
    line-height: 1;
    white-space: nowrap;
  }
  .brand-role {
    position: absolute;
    right: 54px;
    top: 170px;
    margin: 0;
    font-family: "Quicksand", sans-serif;
    font-size: 21px;
    letter-spacing: 1.5px;
    color: var(--ink);
    line-height: 1;
  }
  .card-back {
    position: absolute;
    left: 168px;
    top: 740px;
    width: 520px;
  }
  .contact-list {
    list-style: none;
    margin: 0;
    padding: 0;
    font-family: "Quicksand", sans-serif;
    color: var(--ink);
  }
  .contact-item {
    display: flex;
    align-items: center;
    gap: 6px;
    line-height: 1;
    letter-spacing: 1.5px;
  }
  .contact-item--phone { font-size: 19px; height: 26px; }
  .contact-item--social { font-size: 24px; height: 28px; }
  .contact-item--email { font-size: 24px; height: 30px; }
  .contact-icon { width: 15px; height: 15px; flex: none; }
  .appointment-note {
    margin: 14px 0 0 25px;
    font-family: "Caveat", cursive;
    font-size: 22px;
    color: var(--note-red);
    letter-spacing: 0.5px;
    white-space: nowrap;
  }
</style>
</head>
<body>
<main class="sheet">
  <section class="card-front card-front--one">
    <div class="lipstick-photo" role="img" aria-label="Photograph of a red lipstick tip with a textured smear"></div>
    <h1 class="brand-name">Kolina Varenko</h1>
    <p class="brand-role">Makeup Artist</p>
  </section>

  <section class="card-front card-front--two">
    <div class="lipstick-photo" role="img" aria-label="Photograph of a red lipstick tip with a textured smear"></div>
    <h2 class="brand-name">Kolina Varenko</h2>
    <p class="brand-role">Makeup Artist</p>
  </section>

  <section class="card-back">
    <ul class="contact-list">
      <li class="contact-item contact-item--phone">
        <svg class="contact-icon" viewBox="0 0 16 16" aria-hidden="true">
          <circle cx="8" cy="8" r="7" fill="none" stroke="#111" stroke-width="1.4"/>
          <path d="M5.2 4.3l1.3-.3.8 1.9-.9.7c.4 1 1.1 1.7 2 2.1l.7-.9 1.9.8-.3 1.3c-.2.4-.6.6-1 .6C7 10.3 5.1 8.4 4.6 5.3c0-.4.2-.8.6-1z" fill="#111"/>
        </svg>
        <span>0417305628</span>
      </li>
      <li class="contact-item contact-item--social">
        <svg class="contact-icon" viewBox="0 0 16 16" aria-hidden="true">
          <circle cx="8" cy="8" r="7.5" fill="#111"/>
        </svg>
        <span>Makeup by Kolina</span>
      </li>
      <li class="contact-item contact-item--email">
        <svg class="contact-icon" viewBox="0 0 16 16" aria-hidden="true">
          <rect x="1" y="4" width="14" height="10" fill="#111"/>
          <path d="M1.5 4.5L8 9.5l6.5-5" fill="none" stroke="#fff" stroke-width="1.2"/>
        </svg>
        <span>kolinavarenko@mailpost.com</span>
      </li>
    </ul>
    <p class="appointment-note">Looking forward to our appointment.................................</p>
  </section>
</main>
</body>
</html>
```